K&T Fixit and Rebuild general contracting business card design

I already have a logo that I want to use and I need a card that uses that logo and color scheme on the front with the address phone numbers and email and on the back a place for technicians to write in their name and phone number when they hand it out. It will need the License number of License #KTFXTRB318QN.
It should say General Contractor under the company name. The address is
4417 NE 3rd St, Ste D226
Vancouver, WA 98652
www.kandtfixitandrebuild.example
office@kandtfixitandrebuild.example
360-555-0142 is the telephone number
360-555-0187 is the fax number

Target Market(s)

Homeowners needing remodel work or repairs in their home.

Industry/Entity Type

Construction

Contact Information for Business Card

Business name, address, phone number, license number, fax number, email, and website on the front and a place to fill in technician's name and number

Font styles to use
Serif

Requirements
Must have
• Business name, address, phone number, license number, fax number, email, and website on the front and a place to fill in technician's name and number
Nice to have
• I uploaded an example of a front that is good.
Should not have
• Froo froo or extra embellishments.

```html
<!DOCTYPE html>
<html lang="en">
<head>
<meta charset="utf-8">
<title>K&amp;T Fixit and Rebuild — Business Card</title>
<link href="https://fonts.googleapis.com/css2?family=Source+Serif+4:wght@400;600;700&display=swap" rel="stylesheet">
<style>
  :root {
    --backdrop: #2a2a2a;
    --paper: #fbfbfb;
    --ink-dark: #151515;
    --copper: #b5683a;
    --copper-deep: #9a5229;
    --rule-grey: #8a8a8a;
    --text-light: #f2f2f2;
    --text-muted: #d9d9d9;
  }
  * { box-sizing: border-box; margin: 0; padding: 0; }
  html, body {
    width: 1200px; height: 900px; overflow: hidden;
    background: var(--backdrop);
    font-family: "Source Serif 4", Georgia, serif;
  }
  .stage { position: relative; width: 1200px; height: 900px; }
  .card {
    position: absolute; left: 290px; width: 620px; height: 354px;
    box-shadow: 0 14px 30px rgba(0,0,0,0.45);
  }

  /* Back: technician write-in */
  .card-back { top: 70px; background: var(--paper); }
  .card-back .brand-block {
    position: absolute; top: 62px; left: 0; right: 0; text-align: center;
  }
  .card-back .brand-name {
    color: var(--copper); font-weight: 700; font-size: 38px; line-height: 1.15;
  }
  .card-back .tagline {
    margin-top: 6px; color: var(--copper-deep);
    font-size: 16px; font-weight: 400; letter-spacing: 2px; text-transform: uppercase;
  }
  .write-in {
    position: absolute; left: 52px; right: 52px;
    display: flex; align-items: flex-end; gap: 6px;
  }
  .write-in.name { top: 228px; }
  .write-in.contact { top: 278px; }
  .write-in .label { color: var(--copper-deep); font-size: 17px; font-weight: 600; }
  .write-in .line { flex: 1; border-bottom: 1px solid var(--rule-grey); height: 1px; margin-bottom: 5px; }

  /* Front: contact details */
  .card-front { top: 476px; background: var(--ink-dark); }
  .card-front .brand-block {
    position: absolute; left: 36px; top: 96px; width: 224px;
  }
  .card-front .brand-name {
    color: var(--copper); font-weight: 700; font-size: 34px; line-height: 1.12;
  }
  .card-front .tagline {
    margin-top: 10px; color: var(--text-muted);
    font-size: 13px; letter-spacing: 2px; text-transform: uppercase;
  }
  .divider {
    position: absolute; left: 276px; top: 60px; width: 1.5px; height: 180px;
    background: var(--copper);
  }
  .details {
    position: absolute; left: 296px; top: 62px; right: 16px;
    color: var(--text-light); font-size: 15px; line-height: 1.42;
  }
  .address { margin-bottom: 12px; }
  .contact-row { display: flex; align-items: center; gap: 8px; font-size: 14px; }
  .contact-row svg { width: 13px; height: 13px; flex: none; fill: var(--text-light); }
  .license {
    position: absolute; bottom: 34px; left: 0; right: 0; text-align: center;
    color: var(--text-light); font-size: 17px;
  }
</style>
</head>
<body>
<main class="stage">

  <section class="card card-back">
    <div class="brand-block">
      <h1 class="brand-name">K&amp;T Fixit and Rebuild</h1>
      <p class="tagline">General Contractor</p>
    </div>
    <div class="write-in name"><span class="label">Name:</span><span class="line"></span></div>
    <div class="write-in contact"><span class="label">Contact:</span><span class="line"></span></div>
  </section>

  <section class="card card-front">
    <div class="brand-block">
      <h2 class="brand-name">K&amp;T Fixit<br>and Rebuild</h2>
      <p class="tagline">General Contractor</p>
    </div>
    <div class="divider"></div>
    <div class="details">
      <p class="address">4417 NE 3rd St, Ste D226<br>Vancouver, WA 98652</p>
      <p class="contact-row">
        <svg viewBox="0 0 24 24" aria-hidden="true"><path d="M6.6 10.8a15 15 0 0 0 6.6 6.6l2.2-2.2a1 1 0 0 1 1-.25 11.4 11.4 0 0 0 3.6.57 1 1 0 0 1 1 1V20a1 1 0 0 1-1 1A17 17 0 0 1 3 4a1 1 0 0 1 1-1h3.5a1 1 0 0 1 1 1c0 1.25.2 2.45.57 3.6a1 1 0 0 1-.25 1z"/></svg>
        360-555-0142
      </p>
      <p class="contact-row">
        <svg viewBox="0 0 24 24" aria-hidden="true"><path d="M6 2h12v5H6zM4 8h16a2 2 0 0 1 2 2v7h-4v5H6v-5H2v-7a2 2 0 0 1 2-2zm4 8v4h8v-4z"/></svg>
        360-555-0187
      </p>
      <p class="contact-row">
        <svg viewBox="0 0 24 24" aria-hidden="true"><path d="M2 5h20v14H2zm2 2v.5l8 5 8-5V7z"/></svg>
        office@kandtfixitandrebuild.example
      </p>
      <p class="contact-row">
        <svg viewBox="0 0 24 24" aria-hidden="true"><path d="M12 2a10 10 0 1 0 0 20 10 10 0 0 0 0-20zm0 2a8 8 0 0 1 7.7 6H15a14 14 0 0 0-1.6-5.8A8 8 0 0 1 12 4zm-2 .3A12 12 0 0 0 9 10H4.3A8 8 0 0 1 10 4.3zM4.3 14H9a12 12 0 0 0 1 5.7A8 8 0 0 1 4.3 14zm9.1 5.8A14 14 0 0 0 15 14h4.7a8 8 0 0 1-6.3 5.8z"/></svg>
        www.kandtfixitandrebuild.example
      </p>
    </div>
    <p class="license">License #KTFXTRB318QN</p>
  </section>

</main>
</body>
</html>
```